Dalvrey - Business Card Design

Design a modern masculine business card for our business

Target Market(s)

Private Market

Industry/Entity Type

Construction

Contact Information for Business Card

Company Name - Name of Person - Address - email address - contact number

Font styles to use
Serif
Sans Serif

Colors
0094D4
00A9DD
6FCCEA
C7EBF8
E9F6FB
00AB8E
00BBA5
67D7C9
C6EFE9
E9F9F6
F0912C
F2A743
F7CA91
FBE8D2
FDF5EE

Requirements
Must have
• Use company logo provided
Nice to have
• Company Logo

```html
<!DOCTYPE html>
<html lang="en">
<head>
<meta charset="utf-8">
<title>Dalvrey – Business Card</title>
<link href="https://fonts.googleapis.com/css2?family=Roboto:wght@400;500;900&display=swap" rel="stylesheet">
<style>
  :root {
    --bg: #e4e5e8;
    --card: #ffffff;
    --ink: #111111;
    --muted: #555555;
    --orange: #f26b1d;
    --rule: #f5a06a;
  }
  html, body {
    margin: 0;
    width: 1200px;
    height: 800px;
    overflow: hidden;
    background: var(--bg);
    font-family: "Roboto", Arial, sans-serif;
  }
  .sheet {
    position: relative;
    width: 1200px;
    height: 800px;
    display: flex;
    align-items: center;
    justify-content: center;
    gap: 60px;
  }
  .card {
    position: relative;
    width: 520px;
    height: 297px;
    background: var(--card);
    box-shadow: 0 6px 18px rgba(0,0,0,0.12);
    overflow: hidden;
  }
  .stripe-band {
    position: absolute;
    top: 0;
    bottom: 0;
    width: 12px;
    background: repeating-linear-gradient(
      -60deg,
      var(--orange) 0 22px,
      var(--card) 22px 27px
    );
  }
  .card--front .stripe-band { left: 0; }
  .card--back .stripe-band { right: 0; }

  .wordmark {
    display: flex;
    align-items: center;
    gap: 10px;
    font-weight: 900;
    color: var(--ink);
    letter-spacing: 1px;
    text-transform: uppercase;
    line-height: 1;
    white-space: nowrap;
  }
  .wordmark__square {
    background: var(--orange);
    flex: none;
  }
  .card--front .wordmark {
    position: absolute;
    left: 150px;
    top: 140px;
    font-size: 60px;
  }
  .card--front .wordmark__square { width: 20px; height: 20px; }

  .card--back .wordmark {
    position: absolute;
    left: 40px;
    top: 32px;
    font-size: 46px;
  }
  .card--back .wordmark__square { width: 15px; height: 15px; }

  .person {
    position: absolute;
    left: 40px;
    top: 118px;
    width: 250px;
    padding-bottom: 10px;
    border-bottom: 1px solid var(--rule);
  }
  .person__name {
    margin: 0;
    font-size: 17px;
    font-weight: 500;
    color: var(--orange);
    text-transform: uppercase;
  }
  .person__role {
    margin: 2px 0 0;
    font-size: 14px;
    color: var(--muted);
  }
  .contact {
    position: absolute;
    left: 40px;
    top: 182px;
    width: 300px;
    padding-bottom: 12px;
    border-bottom: 1px solid var(--rule);
    display: flex;
    gap: 14px;
    font-size: 14px;
    color: var(--muted);
    line-height: 1.55;
  }
  .contact__lines { margin: 0; }
  .contact__label { color: var(--orange); margin-right: 4px; }
  .contact__address {
    margin: 0;
    padding-left: 14px;
    border-left: 1px solid var(--rule);
    font-style: normal;
    align-self: flex-end;
  }
</style>
</head>
<body>
<main class="sheet">
  <section class="card card--front" aria-label="Card front">
    <div class="stripe-band"></div>
    <div class="wordmark"><span class="wordmark__square"></span>Dalvrey</div>
  </section>

  <section class="card card--back" aria-label="Card back">
    <div class="stripe-band"></div>
    <div class="wordmark"><span class="wordmark__square"></span>Dalvrey</div>
    <div class="person">
      <p class="person__name">Mark Doyle</p>
      <p class="person__role">Director</p>
    </div>
    <div class="contact">
      <p class="contact__lines">
        <span class="contact__label">T.</span>555-210-4470<br>
        <span class="contact__label">E.</span>info@dalvrey.com
      </p>
      <address class="contact__address">99 dummy city,<br>place 00</address>
    </div>
  </section>
</main>
</body>
</html>
```